Letterhead

We would like to use the logo attached as a new letterhead. Our problem is that we think the dark blue background is too much. We'd like a sleek, professional letterhead, and we'd like at least five options to choose from. I've also uploaded our old letterhead for reference of the style we're going for.

```html
<!DOCTYPE html>
<html lang="en">
<head>
<meta charset="utf-8">
<title>Harbor Line Strategies — Letterhead</title>
<link rel="stylesheet" href="https://fonts.googleapis.com/css2?family=Lato:wght@400;700&family=Roboto:wght@400&family=Allura&display=swap">
<style>
  :root {
    --navy: #1d3050;
    --gold: #c9a762;
    --ink: #3b3b3b;
    --header-ink: #2a3a55;
    --paper: #ffffff;
    --backdrop: #e9e9e9;
  }
  * { margin: 0; padding: 0; box-sizing: border-box; }
  html, body {
    width: 970px; height: 1200px; overflow: hidden;
    background: var(--backdrop);
  }
  .letterhead {
    position: absolute; left: 61px; top: 0;
    width: 848px; height: 1200px;
    background: var(--paper);
    font-family: 'Roboto', Arial, sans-serif;
    color: var(--ink);
  }
  .brand-block {
    position: absolute; left: 0; top: 49px;
    width: 353px; height: 109px;
    background: var(--navy);
    display: flex; align-items: center; gap: 12px;
    padding-left: 60px;
  }
  .brand-mark {
    width: 14px; height: 14px; background: var(--gold);
  }
  .brand-name {
    font-family: 'Lato', Arial, sans-serif;
    font-weight: 700; font-size: 21px; letter-spacing: 1.5px;
    color: #ffffff; line-height: 1.15;
  }
  .accent-bar {
    position: absolute; left: 817px; top: 49px;
    width: 31px; height: 109px; background: var(--gold);
  }
  .company-info {
    position: absolute; left: 392px; top: 78px;
    font-family: 'Lato', Arial, sans-serif;
    font-size: 14.5px; line-height: 19.6px; color: var(--header-ink);
  }
  .company-info .company-name {
    color: var(--gold); font-weight: 700; font-size: 14px;
  }
  .header-divider {
    position: absolute; left: 588px; top: 83px;
    width: 1.5px; height: 52px; background: var(--navy);
  }
  .contact-list {
    position: absolute; left: 633px; top: 80px;
    list-style: none;
    font-family: 'Lato', Arial, sans-serif;
    font-size: 14.5px; line-height: 19.6px; color: var(--header-ink);
  }
  .contact-list li { display: flex; align-items: center; gap: 5px; }
  .contact-list svg { width: 10px; height: 10px; flex: none; }
  .letter-body {
    position: absolute; left: 79px; top: 335px; width: 687px;
    font-size: 13.6px; line-height: 27px; text-align: justify;
  }
  .letter-body p { margin-bottom: 27px; }
  .closing {
    position: absolute; left: 79px; top: 822px;
    font-size: 13.6px; line-height: 27px;
  }
  .signature {
    position: absolute; left: 74px; top: 870px;
    font-family: 'Allura', cursive;
    font-size: 50px; color: #333333;
  }
</style>
</head>
<body>
  <main class="letterhead">
    <header>
      <div class="brand-block">
        <span class="brand-mark"></span>
        <span class="brand-name">HARBOR LINE<br>STRATEGIES</span>
      </div>
      <address class="company-info" style="font-style:normal">
        <div class="company-name">HARBOR LINE STRATEGIES</div>
        <div>218 Cedar Avenue #310</div>
        <div>Juneau, AK 99801</div>
      </address>
      <div class="header-divider"></div>
      <ul class="contact-list">
        <li>
          <svg viewBox="0 0 10 10"><path d="M2 1l2 2-1 1c.6 1.3 1.7 2.4 3 3l1-1 2 2-1.5 1.5C4.5 9 1 5.5.5 2.5z" fill="var(--gold)"/></svg>
          (907) 555-0148
        </li>
        <li>
          <svg viewBox="0 0 10 10"><rect x="0" y="2" width="10" height="7" fill="var(--gold)"/><path d="M0 2l5 4 5-4" stroke="#fff" stroke-width="1" fill="none"/></svg>
          ellen@harborline.com
        </li>
        <li>
          <svg viewBox="0 0 10 10"><circle cx="5" cy="5" r="4.3" fill="none" stroke="var(--gold)" stroke-width="1.2"/><path d="M3 3c1 0 1.5 1 1 2s1 1.5 1 3M6 2c0 1 1 1.5 2 1.5" stroke="var(--gold)" stroke-width="1" fill="none"/></svg>
          harborline.com
        </li>
      </ul>
      <div class="accent-bar"></div>
    </header>

    <section class="letter-body">
      <p>Dear Sir,</p>
      <p>Lorem ipsum dolor sit amet, consectetur adipiscing elit. Aenean ut ipsum eget massa hendrerit vestibulum vel in velit. Donec pretium neque velit.Aliquam porta lectus nec mauris ornare venenatis. Vivamus non est turpis, et cursus sem. Mauris vehicula erat in diam auctor at bibendum nisl lacinia.</p>
      <p>Morbi imperdiet neque vehicula nunc convallis gravida. Vestibulum iaculis pretium placerat. Integer consequat, est sit amet facilisis eleifend, nibh nibh varius orci, eget dapibus arcu dui non purus. Pellentesque in magna mauris. Duis enim sapien, dictum vitae condimentum a, pulvinar vel lacus. Mauris et molestie nibh. Vestibulum vitae nulla at metus elementum porta sit amet interdum elit. Nulla sollicitudin neque eu nulla volutpat congue.</p>
      <p>Etiam pellentesque, velit id dapibus fermentum, turpis sapien ornare dui, ac tincidunt ligula odio congue purus. Nunc sed ante dui, in porta lectus. Cras nec sem lorem. In hac habitasse platea dictumst. Maecenas id diam quis dui porta tristique. Sed id egestas felis. Donec ullamcorper mattis posuere. Phasellus fermentum eleifend tortor vel dapibus. Vestibulum ante ipsum.</p>
    </section>

    <p class="closing">Sincerely,</p>
    <p class="signature">Alan Reed</p>
  </main>
</body>
</html>
```